Business Card and Letterhead for Juniper Anvil - (Have Logo)

Update 4: Removed company reg no from business card details as it looked a bit out of place. Updated services list.
UPDATE 3
Sorry, I got the address a little bit wrong, have updated it below. Sorry for any inconvenience caused.
UPDATE 2
Finally I have the details for the business cards and letterhead. Submissions already made do not have to be updated unless shortlisted, if all new submissions could include the details for me, Marcus, that would be very much appreciated and help with the final shortlist selection. I intend to share a shortlist of the three best entries with past and existing customers for their feedback and opinions. Thank you all again for your time.
Here are the details.
Marcus Telby
Web Developer
T: 01632 960 418
E: marcus@juniperanvil.example
www.juniperanvil.example
Professional Photography
Web Solutions & E-Commerce
Audio & HD Video Production
Marketing & Promotions
Identity and Branding
Juniper Anvil Ltd
Suite 20938, 3rd Floor
212-224 Orchard Lane
London, N7 9QX
Company Reg. No: 05829147
The order and the layout of the information are of course down to the design, but the company registration number should be smaller and less prominent. The formatting of the telephone and email address using a T: and an E: I am not sure about and again if it is Tel: or Email: or Icons is up to the design.
The Company No. on the letterhead should read (somewhere in small text along the bottom):
Juniper Anvil is a Ltd Company registered in England & Wales, Registration No. 05829147.
The second business card details are
Oliver Brackley
Photographer
T: 01632 960 418
E: oliver@juniperanvil.example
Everything else the same of course.
Thank you again for all the submissions so far.
END OF UPDATE 2
-
UPDATE 1: Please do not alter the logo nor the logo colours. (This was a previous pixel forum project and I am extremely happy with it. The icon can stand alone of course, but I have had to eliminate all entries that have made it black and white, or reversed the icon.) I would like to thank everyone that has participated so far and am very grateful for all your thought and time.
End of Update 1
-
Original Brief:
I have attached the logo vector file.
Following a superb logo from a previous Pixel Forum project I am now looking for a business card design and (although less important) a letterhead as well.
I must admit I tried to do it myself but could only come up with the usual amateur stuff that in comparison to the quality of the logo looked awful.
About Us
Juniper Anvil Ltd will be a new company due to start in January. It is really just me (a web developer) and my friend (a photographer). We will be aiming at the usual small to medium sized businesses in the local area, selling various digital services including photographic services to the public, web hosting and development, commercial photography, modelling services (not us!), full video and film production and possibly a bit of marketing as well. (Really it is anything we can do professionally all lumped together! We met running seperate businesses which have both since closed)
We will not be competing on price. We plan to be expensive but fair. Certainly not the cheapest.
What we are looking for
Business Card
I imagine a double sided business card, which will be used for more than one person. I imagine the front to be the same for everyone and the persons details to be on the back, although this is of course only my thoughts and I am of course completely open to any ideas.
The card could also have a services list or a bit about what we do on it. It might feature the website address, our business address (mail forwarding address) or our registered company number.
Or it might have none of that, we are completely open to any ideas and have no real fixed opinions. I just want it to be really nice :-)
Letterhead (secondary importance)
We will make our decision primarily on the business card, although a mathcing letterhead would be fantastic. Something standardish in format and simple, although again, all ideas are welcomed.
I hope that is enough information but if you have any questions I will answer them as fully and as quickly as possible.
Thank you once again and I really look forward to seeing your ideas and picking a winner.
Marcus T.
Small businesses AND the general public
Film Production

```html
<!DOCTYPE html>
<html lang="en">
<head>
<meta charset="utf-8">
<title>Juniper Anvil – Business Card and Letterhead</title>
<link rel="stylesheet" href="https://fonts.googleapis.com/css2?family=Open+Sans:wght@400;600;700;800&display=swap">
<style>
  :root {
    --paper: #ffffff;
    --ink: #1c1c1c;
    --band: #1e1e1e;
    --card-dark: #242424;
    --accent: #c10a14;
    --muted: #333333;
    --shadow: rgba(0,0,0,0.45);
  }
  * { margin: 0; padding: 0; box-sizing: border-box; }
  html, body { width: 1196px; height: 1200px; overflow: hidden; background: var(--paper); }
  body { position: relative; font-family: "Open Sans", Verdana, sans-serif; color: var(--ink); }

  .side-label { position: absolute; top: 0; font-size: 18px; color: var(--muted); letter-spacing: 0.5px; }
  .side-label--front { left: 14px; }
  .side-label--reverse { left: 640px; }

  .sheet { position: absolute; border: 1px solid #000; box-shadow: 8px 8px 8px var(--shadow); overflow: hidden; }

  .wordmark { position: absolute; display: flex; align-items: center; gap: 14px; }
  .wordmark__mark { background: var(--accent); flex: none; }
  .wordmark__name { font-weight: 800; text-transform: uppercase; color: var(--ink); letter-spacing: 1px; white-space: nowrap; }

  .card-front { left: 14px; top: 43px; width: 530px; height: 292px; background: var(--paper); }
  .card-front .wordmark { left: 62px; top: 100px; }
  .card-front .wordmark__mark { width: 40px; height: 40px; }
  .card-front .wordmark__name { font-size: 38px; }
  .holder { position: absolute; left: 0; right: 0; top: 218px; text-align: center; }
  .holder__name { font-size: 21px; font-weight: 700; line-height: 1.2; }
  .holder__role { font-size: 17px; line-height: 1.4; }
  .web-band { position: absolute; left: 0; right: 0; bottom: 0; background: var(--band); color: #fff; text-align: center; }
  .card-front .web-band { height: 48px; line-height: 48px; font-size: 17px; }

  .card-back { left: 640px; top: 43px; width: 548px; height: 294px; background: var(--card-dark); color: #fff; }
  .services__title { position: absolute; left: 50px; top: 38px; font-size: 16px; }
  .services__list { position: absolute; top: 84px; list-style: none; font-size: 11.5px; line-height: 15px; }
  .services__list li::before { content: "* "; }
  .services__list--left { left: 50px; }
  .services__list--right { left: 310px; }
  .contact-band { position: absolute; left: 0; right: 0; top: 216px; height: 33px; background: var(--paper); color: var(--ink); font-size: 16px; line-height: 33px; }
  .contact-band__address { position: absolute; left: 50px; }
  .contact-band__phone { position: absolute; left: 318px; }
  .email-line { position: absolute; left: 0; right: 0; top: 260px; text-align: center; font-size: 16px; }

  .letterhead { left: 10px; top: 364px; width: 615px; height: 824px; background: var(--paper); }
  .letterhead .wordmark { left: 145px; top: 46px; }
  .letterhead .wordmark__mark { width: 30px; height: 30px; }
  .letterhead .wordmark__name { font-size: 29px; }
  .letter-footer { position: absolute; top: 768px; font-size: 16px; }
  .letter-footer--address { left: 93px; }
  .letter-footer--phone { left: 362px; }
  .letterhead .web-band { height: 32px; line-height: 32px; font-size: 17px; }
</style>
</head>
<body>
  <div class="side-label side-label--front">FRONT</div>
  <div class="side-label side-label--reverse">REVERSE</div>

  <section class="sheet card-front" aria-label="Business card front">
    <div class="wordmark">
      <span class="wordmark__mark"></span>
      <span class="wordmark__name">Juniper Anvil</span>
    </div>
    <div class="holder">
      <p class="holder__name">Mr. Marcus Hollen Vance</p>
      <p class="holder__role">Production Manager</p>
    </div>
    <div class="web-band">www.juniperanvil.example</div>
  </section>

  <section class="sheet card-back" aria-label="Business card reverse">
    <p class="services__title">Services:</p>
    <ul class="services__list services__list--left">
      <li>Photography</li>
      <li>Web solutions</li>
      <li>Video production</li>
      <li>Marketing</li>
      <li>Branding</li>
    </ul>
    <ul class="services__list services__list--right">
      <li>Photography</li>
      <li>Web solutions</li>
      <li>Video production</li>
      <li>Marketing</li>
      <li>Branding</li>
    </ul>
    <div class="contact-band">
      <span class="contact-band__address">Birch road 118-C, NY</span>
      <span class="contact-band__phone">(01)555 740 26 93</span>
    </div>
    <p class="email-line">juniper-marcus@mailnest.example</p>
  </section>

  <section class="sheet letterhead" aria-label="Letterhead">
    <div class="wordmark">
      <span class="wordmark__mark"></span>
      <span class="wordmark__name">Juniper Anvil</span>
    </div>
    <p class="letter-footer letter-footer--address">Birch road 118-C, NY</p>
    <p class="letter-footer letter-footer--phone">(01)555 740 26 93</p>
    <div class="web-band">www.juniperanvil.example</div>
  </section>
</body>
</html>
```